Boutique and Spa website design

We need a website for a new business named "Velvet Orchid Boutique and Spa" Base in the state of New York. We sell clothes and accessories as well as spa services:. Microdermabrasion,Peels,Facials,Waxing,Body treatments,.Nails: manicures and pedicures, and massage. We do not sell clothes and accessories on line. I am looking for a spa website.I want this website ready to go. I would like it in HTML/CSS. format.

Target Market(s)

ages 25 to 60

Industry/Entity Type

Business

Font styles to use
Decorative
Script

Colors

Designer to choose colors to be used in the design.

Requirements
Must have
• I want my spa services, my hours, pictures of women getting services (not the pictures below) ,and my logo listed on the website. My hours are Monday and Sunday-Closed and Tues-Friday 10-8....We offer Facials,Microdermabration,Peels,Waxing,eyebrow and eyelash tint, Eyelash extensions, manicure and pedicure, Gel nail polish and shellac,and Massage....Also sell retail skincare products, and women's name brand cloths and accessories...
Nice to have
• Maybe relaxing color tones- browns/purples/greens ....No carton pictures
Should not have
• Prices

```html
<!DOCTYPE html>
<html lang="en">
<head>
<meta charset="utf-8">
<title>Velvet Orchid Boutique and Spa</title>
<link rel="stylesheet" href="https://fonts.googleapis.com/css2?family=Open+Sans:ital,wdth,wght@0,75..100,300..800;1,75..100,300..800&display=swap">
<style>
:root{
  --pink:#dd0f9d;
  --pink-dark:#b50c80;
  --plum:#6a0847;
  --heading:#c0148c;
  --ink:#3a3a3a;
  --paper:#f3f2f3;
  --peach:#fde2c9;
  --dark:#262626;
  --foot-text:#dddddd;
  --teal:#27c6b5;
  --blue:#1d9fe4;
  --white:#ffffff;
  --grey-box:#e6e6e6;
}
*{box-sizing:border-box;margin:0;padding:0}
html,body{width:1200px;height:2356px;overflow:hidden}
body{position:relative;background:var(--paper);font-family:"Open Sans",Arial,sans-serif;color:var(--ink)}
.abs{position:absolute}
a{color:inherit;text-decoration:none}
h1,h2,h3,h4{font-weight:400}

/* header */
.site-header{left:0;top:0;width:1200px;height:155px;background:var(--paper)}
.top-bar{left:0;top:0;width:1200px;height:4px;background:var(--pink)}
.phone-tab{left:729px;top:0;width:302px;height:36px;background:var(--pink);border-radius:0 0 22px 22px;color:var(--white);display:flex;align-items:center;justify-content:center;gap:14px;font-size:26px;font-stretch:80%;letter-spacing:1px}
.brand{left:169px;top:44px;display:flex;align-items:center;gap:10px}
.brand-mark{width:16px;height:16px;background:var(--plum)}
.brand-name{font-size:22px;font-weight:600;color:var(--plum);line-height:1}
.brand-sub{display:block;font-size:10px;letter-spacing:2px;margin-top:4px}
.social{left:916px;top:56px;display:flex;gap:8px}
.social span{width:26px;height:26px;border-radius:50%;background:var(--pink)}
.main-nav{left:619px;top:108px;height:47px;display:flex;font-size:12px;font-stretch:80%;text-transform:uppercase;color:#555}
.main-nav a{display:flex;align-items:center;padding:0 14px;height:47px}
.main-nav a.active{background:var(--pink);color:var(--white)}

/* hero */
.hero{left:0;top:155px;width:1200px;height:373px;background:linear-gradient(90deg,#4a5a3c 0%,#c98c66 25%,#e8b08c 50%,#d79a70 70%,#f1ece6 90%)}
.hero-line{left:0;top:528px;width:1200px;height:4px;background:var(--pink)}
.hero-title{left:711px;top:222px;width:290px;font-size:42px;font-weight:700;font-stretch:75%;color:var(--white);letter-spacing:-1px}
.hero-text{left:711px;top:313px;width:290px;text-align:center;font-size:19px;line-height:27px;color:var(--white)}
.hero-btn{left:766px;top:427px;width:160px;height:41px;background:#3b3b3b;color:var(--white);font-size:22px;font-weight:700;font-stretch:75%;display:flex;align-items:center;justify-content:center}

/* intro */
.intro-photo{left:167px;top:572px;width:276px;height:185px;background:linear-gradient(135deg,#f7f7f2 0%,#9cbd57 45%,#4d6b2a 70%,#2b2b2b 100%)}
.intro-title{left:460px;top:572px;font-size:32px;font-weight:600;font-stretch:75%;color:var(--heading)}
.intro-rule{left:460px;top:614px;width:144px;height:3px;background:var(--heading)}
.intro-text{left:460px;top:626px;width:577px;font-size:12px;line-height:20px;text-align:justify}
.read-more{font-size:12px;color:#444}
.intro-more{left:460px;top:727px}

/* services */
.services{left:0;top:796px;width:1200px;height:505px;background:var(--peach)}
.card{top:852px;width:276px;height:403px;background:var(--white);border-bottom:3px solid var(--pink)}
.card-photo{height:181px}
.card-title{margin-top:30px;text-align:center;font-size:20px;font-stretch:80%;color:#444}
.card-title b{color:var(--heading);font-weight:400}
.card-rule{width:160px;height:2px;background:#d9c2cf;margin:6px auto 0}
.card-text{margin:18px 26px 0;font-size:12.5px;line-height:20px;text-align:center}
.card-more{margin-top:28px;text-align:center}

/* blog */
.blog-title{left:0;top:1350px;width:1200px;text-align:center;font-size:26px;font-stretch:80%;color:var(--heading);letter-spacing:1px}
.blog-rule{left:533px;top:1395px;width:131px;height:3px;background:var(--heading)}
.post{top:1458px;width:282px;display:flex;gap:16px}
.post-date{width:73px;height:63px;flex:none;background:var(--grey-box);border-bottom:6px solid #3a3a3a;font-size:16px;line-height:22px;padding:6px 8px;color:#333}
.post-head{font-size:17px;line-height:22px;color:var(--heading)}
.post-text{font-size:11.5px;line-height:16px;margin-top:12px;text-align:justify}
.pager{top:1588px;width:25px;height:25px;display:flex;align-items:center;justify-content:center}
.pager.prev{left:983px;background:#e8e8e8}
.pager.next{left:1010px;background:var(--blue)}

/* media band */
.media-band{left:0;top:1676px;width:1200px;height:399px;background:linear-gradient(90deg,#b98a68 0%,#dcb08d 45%,#e9c3a4 70%,#c99873 100%)}
.video{left:167px;top:1735px;width:496px;height:279px;background:linear-gradient(180deg,#2a2a2a 0 24px,#6f8e7a 24px,#9cc39f 60%,#4e6fb2 100%)}
.video-play{left:382px;top:1851px;width:64px;height:44px;background:rgba(20,20,20,.85);border-radius:10px;display:flex;align-items:center;justify-content:center}
.video-bar{left:167px;top:1984px;width:496px;height:30px;background:#1f1f1f}
.video-progress{left:172px;top:1983px;width:486px;height:3px;background:#555}
.mail-badge{left:796px;top:1726px;width:182px;height:182px;border-radius:50%;background:var(--pink);display:flex;align-items:center;justify-content:center}
.signup{left:736px;top:1872px;width:299px;height:146px;background:var(--pink);padding:12px 18px;color:var(--white)}
.signup p{font-size:11.5px;line-height:16px}
.signup-field{margin-top:12px;height:30px;background:var(--pink-dark);font-size:11px;padding:8px 12px}
.signup-btn{margin:12px auto 0;width:143px;height:32px;background:var(--plum);font-size:13px;font-stretch:80%;display:flex;align-items:center;justify-content:center}
.band-line{left:0;top:2073px;width:1200px;height:3px;background:var(--teal)}

/* footer */
.site-footer{left:0;top:2076px;width:1200px;height:280px;background:var(--dark)}
.foot-col{top:2120px;font-size:11.5px;color:var(--foot-text)}
.foot-head{color:var(--pink);font-size:12px;font-stretch:80%;text-transform:uppercase;margin-bottom:12px}
.foot-links{list-style:none}
.foot-links li{line-height:22px}
.foot-links li::before{content:"";display:inline-block;width:5px;height:5px;border-radius:50%;background:var(--foot-text);margin-right:12px;vertical-align:middle}
.copyright{margin-top:4px}
.quote{display:flex;gap:14px;margin-bottom:18px;width:260px;line-height:16px}
.avatar{width:42px;height:42px;border-radius:50%;flex:none;background:linear-gradient(#e9d7c8,#a9836a);border:3px solid #eee}
.quote small,.tweet small{display:block;font-size:10px;font-style:italic;margin-top:6px;color:#bbb}
.tweet{width:270px;margin-bottom:16px;line-height:16px}
.view-more{text-decoration:underline;color:#eee}
</style>
</head>
<body>

<header class="site-header abs">
  <div class="top-bar abs"></div>
  <div class="phone-tab abs">
    <svg width="18" height="18" viewBox="0 0 24 24" aria-hidden="true"><path fill="#fff" d="M6.6 10.8a15 15 0 0 0 6.6 6.6l2.2-2.2c.3-.3.7-.4 1-.2 1.1.4 2.3.6 3.6.6.6 0 1 .4 1 1V20c0 .6-.4 1-1 1A17 17 0 0 1 3 4c0-.6.4-1 1-1h3.5c.6 0 1 .4 1 1 0 1.2.2 2.4.6 3.6.1.3 0 .7-.2 1z"/></svg>
    <span>555 0142 377</span>
  </div>
  <div class="brand abs">
    <span class="brand-mark"></span>
    <div class="brand-name">Velvet Orchid<span class="brand-sub">Boutique and Spa</span></div>
  </div>
  <div class="social abs"><span></span><span></span><span></span><span></span></div>
  <nav class="main-nav abs">
    <a class="active" href="#">Home</a><a href="#">About Us</a><a href="#">Packages</a><a href="#">Testimonials</a><a href="#">Contact</a>
  </nav>
</header>

<section>
  <div class="hero abs" role="img" aria-label="Woman with closed eyes receiving a relaxing head massage, white flower beside her"></div>
  <h1 class="hero-title abs">LOREMIPSUMDOLOR</h1>
  <p class="hero-text abs">Lorem Ipsum has been the industry's standard dummy text ever since</p>
  <a class="hero-btn abs" href="#">LOREMIPSUM</a>
  <div class="hero-line abs"></div>
</section>

<section>
  <div class="intro-photo abs" role="img" aria-label="Jars of green spa scrub with leaves and black massage stones"></div>
  <h2 class="intro-title abs">LOREM IPSUM IS SIMPLY DUMMY TEXT</h2>
  <div class="intro-rule abs"></div>
  <p class="intro-text abs">Lorem Ipsum is simply dummy text of the printing and typesetting industry. Lorem Ipsum has been the industry's standard dummy text ever since the 1500s, when an unknown printer took a galley of type and scrambled it to make a type specimen book. It has survived not only five centuries, but also the leap into electronic typesetting, remaining essentially unchanged.</p>
  <a class="read-more intro-more abs" href="#">[ read more ]</a>
</section>

<section class="services abs"></section>
<article class="card abs" style="left:165px">
  <div class="card-photo" role="img" aria-label="Woman resting on a spa table above calm water" style="background:linear-gradient(180deg,#e6d3c2,#c99a7c 60%,#8c6a55)"></div>
  <h3 class="card-title"><b>HEADING</b> GOES HERE</h3><div class="card-rule"></div>
  <p class="card-text">Lorem Ipsum is simply dummy text of the printing and typesetting industry. Lorem Ipsum has been the industry's</p>
  <p class="card-more"><a class="read-more" href="#">[ read more ]</a></p>
</article>
<article class="card abs" style="left:460px">
  <div class="card-photo" role="img" aria-label="Bottles of massage oil with coconuts and palm leaves" style="background:linear-gradient(135deg,#2f4a22,#c9833a 45%,#efe6d6 70%,#3a2a22)"></div>
  <h3 class="card-title"><b>HEADING</b> GOES HERE</h3><div class="card-rule"></div>
  <p class="card-text">Lorem Ipsum is simply dummy text of the printing and typesetting industry. Lorem Ipsum has been the industry's</p>
  <p class="card-more"><a class="read-more" href="#">[ read more ]</a></p>
</article>
<article class="card abs" style="left:759px">
  <div class="card-photo" role="img" aria-label="Hand holding a bowl of warm oil poured onto a back" style="background:linear-gradient(135deg,#f6e1c6,#e9b98a 50%,#c88554)"></div>
  <h3 class="card-title"><b>HEADING</b> GOES HERE</h3><div class="card-rule"></div>
  <p class="card-text">Lorem Ipsum is simply dummy text of the printing and typesetting industry. Lorem Ipsum has been the industry's</p>
  <p class="card-more"><a class="read-more" href="#">[ read more ]</a></p>
</article>

<section>
  <h2 class="blog-title abs">BLOG</h2>
  <div class="blog-rule abs"></div>
  <article class="post abs" style="left:167px">
    <div class="post-date">12 Jan<br>2014</div>
    <div><h3 class="post-head">Lorem Ipsum has been the industry's text</h3><p class="post-text">Lorem Ipsum is simply dummy text of the printing and typesetting industry.</p></div>
  </article>
  <article class="post abs" style="left:459px">
    <div class="post-date">12 Jan<br>2014</div>
    <div><h3 class="post-head">Lorem Ipsum has been the industry's text</h3><p class="post-text">Lorem Ipsum is simply dummy text of the printing and typesetting industry.</p></div>
  </article>
  <article class="post abs" style="left:765px;width:272px">
    <div class="post-date">12 Jan<br>2014</div>
    <div><h3 class="post-head">Lorem Ipsum has been the industry's text</h3><p class="post-text">Lorem Ipsum is simply dummy text of the printing and typesetting industry.</p></div>
  </article>
  <a class="pager prev abs" href="#"><svg width="10" height="12" viewBox="0 0 10 12" aria-hidden="true"><path d="M7 1 2 6l5 5" fill="none" stroke="#bbb" stroke-width="2"/></svg></a>
  <a class="pager next abs" href="#"><svg width="10" height="12" viewBox="0 0 10 12" aria-hidden="true"><path d="M3 1l5 5-5 5" fill="none" stroke="#fff" stroke-width="2"/></svg></a>
</section>

<section>
  <div class="media-band abs" role="img" aria-label="Woman relaxing face down on a massage table reflected in still water"></div>
  <div class="video abs" role="img" aria-label="Embedded video of a spa presenter speaking"></div>
  <div class="video-play abs"><svg width="18" height="20" viewBox="0 0 18 20" aria-hidden="true"><path d="M2 1l15 9-15 9z" fill="#fff"/></svg></div>
  <div class="video-bar abs"></div>
  <div class="video-progress abs"></div>
  <div class="mail-badge abs">
    <svg width="52" height="38" viewBox="0 0 52 38" aria-hidden="true"><rect x="1.5" y="1.5" width="49" height="35" fill="none" stroke="#fff" stroke-width="3"/><path d="M2 2l24 20L50 2M2 36l18-17M50 36 32 19" fill="none" stroke="#fff" stroke-width="3"/></svg>
  </div>
  <form class="signup abs">
    <p>Lorem Ipsum is simply dummy text Lorem Ipsum is simply dummy text of the...</p>
    <div class="signup-field">Email Address</div>
    <div class="signup-btn">SUBMIT</div>
  </form>
  <div class="band-line abs"></div>
</section>

<footer class="site-footer abs"></footer>
<div class="foot-col abs" style="left:165px">
  <h4 class="foot-head">Quick Links</h4>
  <ul class="foot-links"><li>Home</li><li>About Us</li><li>Packages</li><li>Testimonials</li><li>FAQs</li><li>Contact</li></ul>
  <p class="copyright">Copyright © 2014. All right reserved.</p>
</div>
<div class="foot-col abs" style="left:437px">
  <h4 class="foot-head">Testimonial</h4>
  <div class="quote"><div class="avatar" role="img" aria-label="Client portrait"></div><p>Lorem Ipsum has been the industry's standard dummy text<small>John Doe</small></p></div>
  <div class="quote"><div class="avatar" role="img" aria-label="Client portrait"></div><p>Lorem Ipsum has been the industry's standard dummy text<small>John Doe</small></p></div>
  <a class="view-more" href="#">View More</a>
</div>
<div class="foot-col abs" style="left:763px">
  <h4 class="foot-head">Latest Updates</h4>
  <div class="tweet">Lorem Ipsum has been the industry's standard dummy text<small>John Doe &nbsp; - &nbsp; 15 Dec 2013</small></div>
  <div class="tweet">Lorem Ipsum has been the industry's standard dummy text<small>John Doe &nbsp; - &nbsp; 15 Dec 2013</small></div>
  <a class="view-more" href="#">View More</a>
</div>

</body>
</html>
```